Bus Card for Organic Hydroponic Produce company

We need a business card for a budding new business. We grow 100% organic, 100% hydroponic, 100% GMO free produce for sale in our local area. We need something bold and dynamic, not simple and elegant. We want to catch peoples attention and get them to visit our website to view more information about our products and services. Its difficult to explain on a business card the differences between our produce (tomatoes, cucumbers, peppers, etc...) and the kind they would buy at the local grocer or market. , so we need to push them to the website.
We have been brainstorming names for the company and have a few in mind, so choose whichever speaks most to your artistic flair and propose a card based on that one, or both. #1 "Marrowfield Organics" with a slogan something like....." When merely growing green merely isn't quite enough" OR #2 "Quillbrook Organics" with a slogan similar to...."The cutting edge in cleaner, purer organics" OR #3" "Tandrel Organics" with a slogan similar to: "Building a healthier future for those we leave behind"" OR #4 "Loamwise Path" with a slogan similar to: "Purity by Simplicity"
Eventually we will need assistance with web design, promotional and sales materials, etc. so if you offer those services, please indicate that with the design, though it is NOT necessary to offer any additional services to win this contest. WE will pick the winner solely on the business card we like the most.
We want something that stands out, and especially with the name "Oda's organics", we understand that a creative mind may wander into certain attention getting means that may not be quite within the realm of what we can hand out at our local grocer or farmers market. We definitely are not opposed to a little salacious undertone or allusion to attract attention, but please keep it tasteful if you skirt that grey area.
For our card, we use an online printer that can add foils, special die cuts, double sided cards, 3-d cards (we love these 32 pt cards), transparent or translucent cards and more. We love cards that have some of these things where possible and on all of our other business' cards we get rave reviews from customers about their uniqueness. plumtessa.com has the info on these accents if you wish to view what I am referencing.
So in conclusion, we want a unique, stylish, bold, vivid, 2 sided business card that will really stand out. Just usw a generic phone number and website for now and we will add them as they become available. Please email with any questions! Thanks in advance for your effort and creativity!
Target Market(s)
We are targeting parents who are conceintous of what their children and families are eating. Our target audience are moms, but we don't want to exclude anyone else who chooses to eat more healthy. Our target customer is the same customer that would shop at Brightcart stores or local farmers markets

```html
<!DOCTYPE html>
<html lang="en">
<head>
<meta charset="utf-8">
<title>Fernvaleorganics business card</title>
<link rel="stylesheet" href="https://fonts.googleapis.com/css2?family=Lato:ital,wght@0,400;0,700;0,900;1,700&display=swap">
<style>
  :root {
    --page: #ece9e4;
    --card: #ffffff;
    --leaf: #8cc63f;
    --leaf-dark: #7ab62e;
    --berry: #d9262c;
    --ink: #2b2b2b;
    --slate: #555a5e;
  }
  * { box-sizing: border-box; margin: 0; padding: 0; }
  html, body {
    width: 915px; height: 1200px; overflow: hidden;
    background: var(--page);
    font-family: "Lato", Arial, sans-serif;
  }
  .card {
    position: absolute; left: 70px;
    width: 776px; height: 454px;
    background: var(--card);
    box-shadow: 0 2px 10px rgba(0,0,0,.18);
    overflow: hidden;
  }
  .card--front { top: 120px; }
  .card--back { top: 690px; }
  .swoosh { position: absolute; inset: 0; width: 100%; height: 100%; }

  .brand {
    position: absolute; left: 0; right: 0;
    display: flex; justify-content: center; align-items: center; gap: 10px;
  }
  .brand__mark { width: 14px; height: 14px; border-radius: 50%; background: var(--leaf); }
  .brand__name {
    font-weight: 900; color: var(--berry); letter-spacing: -0.5px; line-height: 1;
  }
  .tagline {
    position: absolute; left: 0; right: 0; text-align: center;
    font-weight: 700; font-style: italic; letter-spacing: 0.6px;
  }

  .card--front .brand { top: 62px; left: 120px; right: 0; justify-content: flex-start; padding-left: 100px; }
  .card--front .brand__name { font-size: 50px; }
  .card--front .tagline { top: 122px; left: 212px; right: auto; font-size: 20px; color: var(--slate); }

  .contact { position: absolute; left: 44px; font-size: 18px; line-height: 31px; color: var(--ink); }
  .contact--address { top: 208px; }
  .contact--online { top: 326px; }

  .phone {
    position: absolute; left: 472px; top: 346px;
    font-size: 21px; font-weight: 700; color: #fff;
  }

  .card--back .brand { top: 180px; }
  .card--back .brand__name { font-size: 58px; }
  .card--back .brand__mark { width: 16px; height: 16px; }
  .card--back .tagline { top: 246px; font-size: 23px; color: var(--leaf); }
</style>
</head>
<body>
  <section class="card card--front">
    <svg class="swoosh" viewBox="0 0 776 454" aria-hidden="true">
      <path d="M70 454 C 380 436, 640 320, 776 118 L 776 454 Z" fill="var(--leaf)"/>
      <path d="M92 454 C 390 430, 630 330, 776 150" fill="none" stroke="#a6d46a" stroke-width="2" opacity=".5"/>
      <path d="M372 426 C 540 392, 680 270, 728 62 L 744 70 C 700 280, 560 402, 372 426 Z" fill="var(--berry)"/>
      <polygon points="776,2 700,36 722,52 734,46 746,74" fill="var(--berry)"/>
    </svg>
    <div class="brand"><span class="brand__name">Fernvaleorganics</span><span class="brand__mark"></span></div>
    <p class="tagline">A new standard in organic produce</p>
    <address class="contact contact--address" style="font-style:normal">
      Address: 123 Main Street,<br>Larkmoor Bay, VA 23456
    </address>
    <p class="contact contact--online">Odasorganics@mailnest.com<br>www.OdasOrganics.com</p>
    <p class="phone">Phone:555-555-5555</p>
  </section>

  <section class="card card--back">
    <div class="brand"><span class="brand__name">Fernvaleorganics</span><span class="brand__mark"></span></div>
    <p class="tagline">A new standard in organic produce</p>
  </section>
</body>
</html>
```